Company providing Business Management Services needs modern business card

The business provides services like tender preparation, bank submissions, business health checks, financial and admin support. We want to portray 'Trust', 'Strength' and 'Support'.
2 styles of logo in various formats have been uploaded.
Looking for easy to understand, yet sophisticated and stand out from the crowd.

Target Market(s)

Small and Medium sized businesses

Industry/Entity Type

Business

Contact Information for Business Card

Name - Daniel Vesterby, Description - Manager, Phone - 0472 915 603, Email - danielvesterby@kpwholdingsgroup.example, Work description - Business Management Services.

Requirements
Must have
• Logo

```html
<!DOCTYPE html>
<html lang="en">
<head>
<meta charset="utf-8">
<title>KPW Holdings Group – Business Card</title>
<link rel="stylesheet" href="https://fonts.googleapis.com/css2?family=Poppins:wght@300;400;600&display=swap">
<style>
  :root {
    --page-bg: #e6e8e8;
    --card-white: #ffffff;
    --panel-dark: #1f1e1f;
    --panel-mid: #3a393b;
    --ink-dark: #454547;
    --ink-grey: #8a8a8c;
    --ink-light: #b9b9bb;
    --map-tone: #eeeeef;
  }
  * { box-sizing: border-box; margin: 0; padding: 0; }
  html, body {
    width: 1200px; height: 1000px; overflow: hidden;
    background: var(--page-bg);
    font-family: "Poppins", sans-serif;
  }
  .canvas {
    width: 1200px; height: 1000px;
    display: flex; align-items: center; justify-content: center;
  }
  .business-card {
    width: 900px; height: 514px;
    display: flex;
    background: var(--card-white);
    box-shadow: 0 10px 30px rgba(0,0,0,0.18);
    overflow: hidden;
  }
  .identity-panel {
    width: 360px;
    background: linear-gradient(160deg, var(--panel-dark) 0%, var(--panel-dark) 55%, var(--panel-mid) 100%);
    padding: 70px 50px 56px;
    display: flex; flex-direction: column; justify-content: space-between;
  }
  .brand-mark {
    display: flex; align-items: center; gap: 16px;
  }
  .brand-mark .mark-square {
    width: 96px; height: 96px; flex: none;
    background: #bdbdbf;
  }
  .holder-name {
    color: var(--card-white);
    font-size: 27px; font-weight: 600; line-height: 1.2;
  }
  .holder-role {
    color: var(--ink-light);
    font-size: 21px; font-weight: 300; margin-top: 4px;
  }
  .contact-panel {
    position: relative;
    flex: 1;
    padding: 56px 50px 56px 48px;
    display: flex; flex-direction: column;
  }
  .map-backdrop {
    position: absolute; right: 30px; top: 150px;
    width: 420px; height: 230px;
    background: radial-gradient(ellipse at center, var(--map-tone) 0%, rgba(238,238,239,0.4) 60%, rgba(255,255,255,0) 100%);
  }
  .company-name {
    position: relative;
    color: var(--ink-dark);
    font-size: 46px; font-weight: 600; line-height: 1.08;
    letter-spacing: -0.5px;
  }
  .contact-details {
    position: relative;
    margin-top: auto;
    color: var(--ink-dark);
    font-weight: 300;
  }
  .contact-phone { font-size: 25px; letter-spacing: 1px; }
  .contact-email { font-size: 17px; margin-top: 2px; }
  .service-line {
    position: relative;
    margin-top: 30px;
    color: var(--ink-grey);
    font-size: 21px; font-weight: 600;
  }
</style>
</head>
<body>
<main class="canvas">
  <article class="business-card">
    <section class="identity-panel">
      <div class="brand-mark">
        <span class="mark-square"></span>
      </div>
      <div class="holder">
        <p class="holder-name">Daniel Vesterby</p>
        <p class="holder-role">Manager</p>
      </div>
    </section>
    <section class="contact-panel">
      <div class="map-backdrop" role="img" aria-label="Faint dotted world map backdrop"></div>
      <h1 class="company-name">KPW Holdings<br>Group</h1>
      <div class="contact-details">
        <p class="contact-phone">0472 915 603</p>
        <p class="contact-email">danielvesterby@kpwholdingsgroup.example</p>
      </div>
      <p class="service-line">Business Management Services.</p>
    </section>
  </article>
</main>
</body>
</html>
```